Website Design Front page Holistic Members site & Natural Therapist Directory

I need a modern, fresh unique look for a natural therapy and holistic/ Spiritual directory & educational website. It needs to be clear, colourful, inviting and suitable for both sexes - young and old. I want it look fresh and super modern.

I will require the design in .psd format and anything in the centre section including rotational image needs to be supplied in .ai so I can break down the components and colours used will also be needed for frames and banners.

Target Market(s)

all ages, male and female. It must appeal to both therapists and general public.

Requirements
Must have
• Logo obviously. Room for a video player 300 x 250. And small introduction text panel. Must follow the layout in file attached. Also a rotating image up the top, in main section (have supplied example image alter as you like - man pointing top right). Have also supplied example of text to have on it. 16 Menu bars on left frame, under home. Must have 6 prominent links to main pages of site. Have included images use if you want or else use your own. These 6 are, Find a Psychic/ Medium, Find a Natural Therapist, Find a Business/ Club/ School, Find an Event/ Workshop, Find a Product, Holistic Career Centre.I have also attached a shot of the emag, although nothing special in design, useful for complimentary colour choices but not limited to. Another link image/ banner would be Free Chat Now.Another if room and not over crowded would be compare memberships. Can use leader board and leader ad board. Also require the footer to be designed and delivered in .ai similar to craft pebble with link image to chatterly and blurbo.
Nice to have
• Compare memberships link would be great but not essential... don't want page to look too busy.
Should not have
• Must not be too busy.. think zen with a modern twist.

```html
<!DOCTYPE html>
<html lang="en">
<head>
<meta charset="utf-8">
<title>Soulful Echo – Holistic Directory</title>
<link rel="stylesheet" href="https://fonts.googleapis.com/css2?family=Arimo:wght@400;700&family=Signika:wght@400;600&family=Noto+Serif:wght@700&family=Anton&display=swap">
<style>
:root{
  --green-dark:#2f8a12;
  --green-mid:#5cc02a;
  --green-light:#d6f3e6;
  --orange:#e8701a;
  --orange-light:#f7a33a;
  --orange-btn:#f39a22;
  --magenta:#a0147f;
  --magenta-light:#c42aa3;
  --blue:#2f9fe0;
  --blue-light:#4bb8ee;
  --blue-dark:#1c7fc4;
  --pink:#e0338f;
  --text-grey:#6b6b6b;
  --heading-grey:#8a8a8a;
  --white:#ffffff;
  --navy:#0f3b57;
}
*{box-sizing:border-box;margin:0;padding:0}
html,body{width:1052px;height:1200px;overflow:hidden}
body{
  position:relative;font-family:"Arimo",Arial,sans-serif;color:var(--text-grey);
  background:
    linear-gradient(180deg,var(--green-dark) 0%,var(--green-mid) 6%,#a8e3b4 11%,var(--green-light) 15%,#f4fbf7 22%,#ffffff 40%,#ffffff 72%,#e8f7ec 80%,#9bd875 87%,var(--green-mid) 92%,var(--green-dark) 100%);
}
.abs{position:absolute}
a{color:inherit;text-decoration:none}

/* header */
.brand{left:28px;top:70px;display:flex;align-items:center;gap:10px}
.brand-dot{width:26px;height:26px;border-radius:50%;background:var(--magenta-light)}
.brand-name{font-family:"Signika",sans-serif;font-weight:600;font-size:40px;color:#2c2c2c;line-height:1}
.chat-btn{left:830px;top:42px;width:216px;height:64px}
.chat-photo{left:0;top:0;width:64px;height:64px;border-radius:50%;background:radial-gradient(circle,#f0c79a,#b5763f);border:3px solid #f6c04a;z-index:2}
.chat-pill{left:40px;top:18px;width:176px;height:38px;border-radius:6px 19px 19px 6px;background:linear-gradient(180deg,var(--blue-light),var(--blue-dark));padding:3px 0 0 32px;color:var(--white);font-weight:700}
.chat-pill small{display:block;font-size:11px;line-height:12px;color:#10304a}
.chat-pill span{display:block;font-size:19px;line-height:20px}

.topbar{left:6px;top:158px;width:1040px;height:46px;border-radius:16px 16px 0 0;background:linear-gradient(180deg,#fbe3cf 0%,var(--orange-light) 12%,var(--orange) 60%,#d45f10 100%);border:2px solid #f4f0ea}
.topbar-links{right:28px;top:15px;font-size:11px;color:var(--white)}
.topbar-links a{padding:0 7px}

/* panels */
.panel-title{font-size:15px;color:var(--white);padding:10px 12px;font-family:"Arimo",sans-serif}
.panel-magenta{background:linear-gradient(180deg,var(--magenta-light),var(--magenta));border-radius:10px 10px 0 0}
.search{left:6px;top:212px;width:187px;height:92px}
.search input{display:block;margin:2px 0 0 12px;width:164px;height:17px;border:1px solid #999}
.search button{display:block;margin:7px 0 0 12px;width:92px;height:20px;background:linear-gradient(180deg,var(--orange-light),var(--orange));border:1px solid #fff;color:#222;font:700 11px "Arimo",sans-serif;text-align:left;padding-left:6px}

.side-menu{left:6px;top:305px;width:187px;list-style:none}
.side-menu li{height:27.3px;line-height:25px;border:1px solid #a8d8f4;background:linear-gradient(180deg,var(--blue-light),var(--blue));color:var(--white);font:600 12px "Signika",sans-serif;padding-left:22px;margin-bottom:0}
.side-menu li.active{background:linear-gradient(180deg,#ffc15a,var(--orange-btn));}

.featured{left:6px;top:776px;width:187px;height:236px;border-radius:0 0 10px 10px;background:linear-gradient(180deg,var(--magenta-light),var(--magenta))}
.featured .panel-title{padding:16px 14px 10px;border-bottom:1px solid #d572c0}
.featured-photo{left:32px;top:50px;width:124px;height:106px;background:linear-gradient(180deg,#d8b68a,#f0d8c0);border:1px solid #222}
.featured-name{top:165px;width:100%;text-align:center;font:700 11px "Arimo",sans-serif;color:var(--white);text-decoration:underline}
.featured-note{top:193px;width:100%;text-align:center;font:600 12px/14px "Signika",sans-serif;color:var(--white);border-top:1px solid #d572c0;padding-top:5px}

/* hero */
.hero{left:206px;top:212px;width:614px;height:296px;background:var(--navy);padding:6px}
.hero-photo{width:100%;height:100%;background:linear-gradient(180deg,#3a9ee0 0%,#8cc8ef 55%,#2f85c8 62%,#e9f1f4 66%,#ffffff 100%);border:1px solid #7fb6d8}
.hero-links{left:560px;top:247px;width:272px;list-style:none}
.hero-links li{height:36px;line-height:34px;margin-bottom:0;border-bottom:1px solid #bfe3f7;background:linear-gradient(180deg,var(--blue-light),var(--blue));color:var(--white);font:600 16px "Signika",sans-serif;padding-left:10px}
.hero-links li.active{background:linear-gradient(180deg,#f06ab0,var(--pink))}
.hero-arrow{left:544px;top:255px}

/* intro */
.intro{left:210px;top:525px;width:610px}
.intro h1{font:700 24px "Noto Serif",serif;color:var(--heading-grey);padding-bottom:10px;border-bottom:1px dashed #999}
.intro h2{font:700 18px "Noto Serif",serif;color:var(--heading-grey);padding-bottom:8px;border-bottom:1px dashed #999;margin-top:22px}
.intro p{font-size:10.5px;line-height:12.5px;margin-top:8px}
.intro .col{width:262px;margin-top:14px}

.video{left:496px;top:724px;width:316px;height:266px;border-radius:10px;background:#000;border:3px solid #d8d8d8;box-shadow:0 0 0 1px #555}
.video-icon{left:90px;top:48px}
.video-bar{left:0;bottom:0;width:100%;height:28px;background:linear-gradient(180deg,#e6e6e6,#9a9a9a);border-radius:0 0 7px 7px}

/* right column */
.profile{left:838px;top:212px;width:208px;height:263px;background:var(--magenta);border-radius:10px 10px 0 0}
.profile ul{list-style:none}
.profile li{height:25.2px;line-height:24px;border-bottom:1px solid #c24aa8;background:linear-gradient(180deg,var(--magenta-light),var(--magenta));color:var(--white);font:600 12px "Signika",sans-serif;padding-left:28px}
.panel-blue{background:var(--blue);border:1px solid #7fc6ef}
.panel-blue .panel-title{background:linear-gradient(180deg,var(--blue-light),var(--blue));border-bottom:1px solid #86cdf2}
.events{left:838px;top:484px;width:208px;height:154px}
.event{padding:8px 0 0 22px;color:var(--white)}
.event small{display:block;font-size:11px}
.event a{font-size:14px;text-decoration:underline}
.news{left:838px;top:646px;width:208px;height:234px}
.news-item{padding:9px 0 0 22px;color:#111;font:700 12px "Noto Serif",serif}
.news-item a{display:block;font:400 10px "Arimo",sans-serif;color:var(--white);text-decoration:underline}
.news-btn{left:22px;top:186px;width:166px;height:34px;background:linear-gradient(180deg,#ffc15a,var(--orange-btn));border:1px solid #fff;color:#222;font-size:14px;text-align:center;line-height:32px}
.compare{left:838px;top:888px;width:208px;height:182px;background:linear-gradient(180deg,#eaeaea,#cfcfcf);border:1px solid #c9c9c9}
.compare .panel-title{font-size:14px;text-align:center}
.compare-text{top:68px;width:100%;text-align:center;font:30px/32px "Anton",sans-serif;color:var(--white);background:#0c2a4a00;-webkit-text-fill-color:var(--white);text-shadow:0 0 0 #000}
.compare-band{left:10px;top:64px;width:188px;height:106px;background:#13304f;border-radius:6px}

/* footer */
.footer-links{left:8px;top:1133px;font:600 12px "Signika",sans-serif;color:var(--white)}
.footer-links a{padding:0 9px}
.footer-links a:first-child{padding-left:0}
.find-us{left:850px;top:1100px;font:600 11px "Signika",sans-serif;color:var(--white)}
.socials{left:856px;top:1122px;display:flex;gap:6px}
.social{display:flex;flex-direction:column;align-items:center;gap:3px;font:600 9px "Signika",sans-serif;color:var(--white)}
.social i{display:block;width:28px;height:28px;border-radius:5px;background:rgba(255,255,255,.85)}
.copyright{left:0;top:1178px;width:1052px;text-align:center;font:600 12px "Signika",sans-serif;color:var(--white)}
</style>
</head>
<body>

<header>
  <div class="abs brand"><span class="brand-dot"></span><span class="brand-name">Soulful Echo</span></div>
  <a class="abs chat-btn" href="#">
    <div class="abs chat-photo" role="img" aria-label="Support agent wearing a headset"></div>
    <div class="abs chat-pill"><small>Click Here For</small><span>FREE CHAT</span></div>
  </a>
  <nav class="abs topbar">
    <div class="abs topbar-links"><a href="#">Contact Us</a>|<a href="#">Sign In</a>|<a href="#">Register</a></div>
  </nav>
</header>

<aside>
  <form class="abs search panel-magenta">
    <div class="panel-title">COMMUNITY SEARCH</div>
    <input type="text" aria-label="Search">
    <button type="button">Search</button>
  </form>
  <ul class="abs side-menu">
    <li class="active">Home</li><li>About Us</li><li>Contact Us</li><li>Feng Shui</li><li>Yoga &amp; Meditation</li><li>Tarot</li><li>Numerology</li><li>Chakras</li><li>Book Club</li><li>Give Aways</li><li>Healthy Recipes</li><li>EXCLUSIVE INTERVIEWS</li><li>Guest Psychic</li><li>More menu</li><li>more menu</li><li>more menu</li><li>more menu</li>
  </ul>
  <section class="abs featured">
    <div class="panel-title">FEATURED MEMBERS</div>
    <div class="abs featured-photo" role="img" aria-label="Portrait photo of the featured member"></div>
    <div class="abs featured-name">MARION K. HALE</div>
    <div class="abs featured-note">Volunteer of the year<br>Recipient award winner</div>
  </section>
</aside>

<main>
  <div class="abs hero"><div class="hero-photo" role="img" aria-label="Man in white seated on a cushion by the sea, pointing to the upper right"></div></div>
  <svg class="abs hero-arrow" width="18" height="20" aria-hidden="true"><polygon points="18,0 0,10 18,20" fill="#e0338f"/></svg>
  <ul class="abs hero-links">
    <li class="active">Find a Psychic/ Medium</li>
    <li>Find a Natural Therapist</li>
    <li>Find a Business/ Club/ School</li>
    <li>Find an Event/ Workshop</li>
    <li>Find a Product</li>
    <li>Holistic Career Centre</li>
  </ul>

  <article class="abs intro">
    <h1>Lorem ipsum dolor sit amet</h1>
    <p>Donec nisi eros, venenatis feugiat lacinia vitae, vestibulum et elit. Sed sollicitudin aliquam ipsum, et rhoncus purus tincidunt in. Aliquam nec nulla neque, non rhoncus velit. Aenean porta consectetur lacinia. Sed sit amet diam id purus blandit congue. Cras convallis nisi massa, nec eleifend erat. Nam ac eros sit amet urna pretium ultricies eu congue est. Aenean vitae magna eu ligula adipiscing tempus non sit amet felis. In hac habitasse platea dictumst. Nullam mollis malesuada consectetur. Aenean sed ligula velit. Aenean eu nulla eget mi pellentesque molestie. Vestibulum tempor luctus magna,</p>
    <h2>Lorem ipsum dolor sit amet</h2>
    <p class="col">Donec nisi eros, venenatis feugiat lacinia vitae, vestibulum et elit. Sed sollicitudin aliquam ipsum, et rhoncus purus tincidunt in. Aliquam nec nulla neque, non rhoncus velit. Aenean porta consectetur lacinia. Sed sit amet diam id purus blandit congue. Cras convallis nisi massa, lobortis vehicula eleifend. Morbi vestibulum, ligula vitae sagittis facilisis, metus leo elementum purus.</p>
  </article>

  <div class="abs video">
    <svg class="abs video-icon" width="150" height="110" viewBox="0 0 150 110" aria-hidden="true">
      <circle cx="52" cy="52" r="48" fill="none" stroke="#fff" stroke-width="5"/>
      <circle cx="52" cy="26" r="12" fill="#fff"/><circle cx="52" cy="78" r="12" fill="#fff"/>
      <circle cx="26" cy="52" r="12" fill="#fff"/><circle cx="78" cy="52" r="12" fill="#fff"/>
      <circle cx="52" cy="52" r="6" fill="none" stroke="#fff" stroke-width="3"/>
      <path d="M88 80 Q110 120 140 96" fill="none" stroke="#fff" stroke-width="4"/>
    </svg>
    <div class="abs video-bar">
      <svg width="310" height="28" aria-hidden="true">
        <rect x="6" y="6" width="20" height="16" fill="#555"/><rect x="32" y="6" width="20" height="16" fill="#555"/><rect x="58" y="6" width="20" height="16" fill="#555"/>
        <polygon points="13,10 13,18 18,14" fill="#fff"/><rect x="38" y="10" width="3" height="8" fill="#fff"/><rect x="43" y="10" width="3" height="8" fill="#fff"/><polygon points="64,10 64,18 69,14" fill="#fff"/>
        <rect x="92" y="8" width="140" height="12" fill="#111"/>
        <rect x="240" y="9" width="30" height="10" fill="#444"/>
        <polygon points="282,10 288,10 294,6 294,22 288,18 282,18" fill="#222"/>
      </svg>
    </div>
  </div>
</main>

<aside>
  <section class="abs profile">
    <div class="panel-title">MY PROFILE</div>
    <ul><li>Profile Home</li><li>Manage Profiles</li><li>Networks</li><li>Files &amp; Links</li><li>Favorites</li><li>Messages</li><li>Connections</li><li>Refer A Friend</li></ul>
  </section>
  <section class="abs events panel-blue">
    <div class="panel-title">EVENTS CALENDER</div>
    <div class="event"><small>10/01/2011</small><a href="#">TECH CONF 2010</a></div>
    <div class="event"><small>10/09/2010</small><a href="#">WEB DEV CONF 2010</a></div>
  </section>
  <section class="abs news panel-blue">
    <div class="panel-title">LATEST NEWS</div>
    <div class="news-item">10/01/2011<a href="#">General Tech News Today</a></div>
    <div class="news-item">10/01/2011<a href="#">General Tech News Today</a></div>
    <div class="news-item">10/01/2011<a href="#">General Tech News Today</a></div>
    <a class="abs news-btn" href="#">More News</a>
  </section>
  <section class="abs compare">
    <div class="panel-title panel-magenta" style="border-radius:0">COMPARE MEMBERSHIP</div>
    <div class="abs compare-band"></div>
    <div class="abs compare-text">COMPARE OUR<br>MEMBERSHIP<br>WITH OTHERS</div>
  </section>
</aside>

<footer>
  <nav class="abs footer-links"><a href="#">Home</a>|<a href="#">About Us</a>|<a href="#">Contact Us</a>|<a href="#">SItemap</a>|<a href="#">Terms &amp; Conditions</a>|<a href="#">Privacy Policy</a></nav>
  <div class="abs find-us">Find Us On:</div>
  <div class="abs socials">
    <span class="social"><i></i>snapwell</span>
    <span class="social"><i></i>chatterly</span>
    <span class="social"><i></i>linkhub</span>
    <span class="social"><i></i>blurbo</span>
    <span class="social"><i></i>rss</span>
  </div>
  <div class="abs copyright">© Copyright , soulfulecho.com &nbsp;&nbsp;|&nbsp;&nbsp; All Rights Reserved</div>
</footer>

</body>
</html>
```